law firm business cards

I need a business card using my existing logo. Two sided is best because there is a lot of information that needs to go on the card. Use the same general color scheme as logo, but I need one set with the blue background of my website (www.halvorsenlawgrp.com), and one set with white background (to see which one I like best).

Information that must be on there:
Trevor J. Halvorsen
Board Certified Civil Trial Specialist
738 Brinkley Ave., Suite 640
Raleigh, NC 27601

T 919-555-0143
F 919-555-0176

www.halvorsenlawgrp.com
trevor@halvorsenlawgrp.com

Personal Injury | Criminal Law (to separate the two, pls use a bullet point or pipeline symbol "|"

If there is a way to work in the CPRS logo (maybe at the bottom somewhere), put it in, but don't let it detract from the main logo too much.

Also, if there is a way to work it in, put in somewhere: Former Insurance Company Attorney | Former Criminal Prosecutor (to separate the two, pls use a bullet point or pipeline symbol "|"

```html
<!DOCTYPE html>
<html lang="en">
<head>
<meta charset="utf-8">
<title>Halvorsen Law — Business Cards</title>
<link href="https://fonts.googleapis.com/css2?family=Cinzel:wght@400;500&family=Questrial&display=swap" rel="stylesheet">
<style>
  :root {
    --page: #eceef0;
    --navy: #2e3b6e;
    --navy-deep: #24305c;
    --ink: #1f2a55;
    --sky: #6f8fcf;
    --red: #d8283a;
    --paper: #ffffff;
    --muted: #c9d1e6;
  }
  * { margin: 0; padding: 0; box-sizing: border-box; }
  html, body { width: 1200px; height: 800px; overflow: hidden; }
  body {
    background: var(--page);
    position: relative;
    font-family: "Questrial", "Helvetica Neue", Arial, sans-serif;
  }
  .card {
    position: absolute;
    width: 520px;
    height: 298px;
    border-radius: 3px;
    overflow: hidden;
    box-shadow: 0 6px 18px rgba(30, 40, 70, 0.18);
  }
  /* Front: blue */
  .card--front {
    left: 60px; top: 251px;
    background: linear-gradient(160deg, var(--navy) 0%, var(--navy-deep) 100%);
    color: var(--paper);
    border-bottom: 6px solid var(--red);
  }
  .brand {
    display: flex; align-items: center; gap: 10px;
    font-family: "Cinzel", Georgia, serif;
    font-weight: 500;
    letter-spacing: 1px;
  }
  .brand__mark { width: 12px; height: 12px; background: currentColor; flex: none; }
  .card--front .brand { position: absolute; left: 34px; top: 30px; font-size: 30px; color: var(--paper); }
  .front__name {
    position: absolute; left: 34px; top: 118px;
    font-family: "Cinzel", Georgia, serif;
    font-size: 27px; letter-spacing: 1.5px; font-weight: 400;
  }
  .front__title {
    position: absolute; left: 35px; top: 156px;
    font-size: 14.5px; letter-spacing: 1.2px; text-transform: uppercase;
  }
  .front__contact {
    position: absolute; left: 35px; top: 196px;
    list-style: none; font-size: 13.5px; line-height: 22px; letter-spacing: 0.4px;
    color: var(--muted);
  }
  .front__contact .sep { padding: 0 6px; }
  /* Back: white */
  .card--back {
    left: 620px; top: 251px;
    background: var(--paper);
    color: var(--ink);
    border-bottom: 6px solid var(--sky);
  }
  .card--back .brand {
    position: absolute; left: 0; right: 0; top: 52px;
    justify-content: center; font-size: 22px; color: var(--ink);
  }
  .back__practice {
    position: absolute; left: 0; right: 0; top: 112px; text-align: center;
    font-family: "Cinzel", Georgia, serif;
    font-size: 25px; letter-spacing: 1px;
  }
  .back__history {
    position: absolute; left: 0; right: 0; top: 166px; text-align: center;
    list-style: none; font-size: 14px; line-height: 24px; letter-spacing: 1.3px;
    text-transform: uppercase; color: #3b4a80;
  }
  .back__seal { position: absolute; right: 30px; bottom: 20px; }
</style>
</head>
<body>
  <section class="card card--front" aria-label="Business card, front">
    <div class="brand"><span class="brand__mark"></span>Halvorsen Law</div>
    <h1 class="front__name">Trevor J. Halvorsen</h1>
    <p class="front__title">Board Certified Civil Trial Specialist</p>
    <ul class="front__contact">
      <li>738 Brinkley Ave., Suite 640<span class="sep">,</span>Raleigh, NC 27601</li>
      <li>T 919-555-0143<span class="sep">·</span>F 919-555-0176</li>
      <li>www.halvorsenlawgrp.com<span class="sep">·</span>trevor@halvorsenlawgrp.com</li>
    </ul>
  </section>

  <section class="card card--back" aria-label="Business card, back">
    <div class="brand"><span class="brand__mark"></span>Halvorsen Law</div>
    <h2 class="back__practice">Personal Injury · Criminal Law</h2>
    <ul class="back__history">
      <li>Former Insurance Company Attorney</li>
      <li>Former Criminal Prosecutor</li>
    </ul>
    <svg class="back__seal" width="54" height="54" viewBox="0 0 54 54" role="img" aria-label="CPRS certification badge">
      <circle cx="27" cy="27" r="25" fill="none" stroke="#2e3b6e" stroke-width="1.5"/>
      <circle cx="27" cy="27" r="19" fill="none" stroke="#2e3b6e" stroke-width="1"/>
    </svg>
  </section>
</body>
</html>
```